Broschüre für Gleichstellungsstelle einer kommunalen Stadtverwaltung
Zielgruppe
Wir sind die Gleichstellungsstelle einer kommunalen Stadtverwaltung (Einwohner*innen ca. 74.500) und richten uns mit unserer Arbeit grundsätzlich an alle Menschen.
Wir wollen eine Broschüre zum Handlungsleitfaden für die geschlechtergerechte Sprache bei der Stadt erstellen. Dieser soll an die Beschäftigten als Unterstützung verteilt werden.
Aufgabenstellung
- Broschüre mit Wire-O-Bindung, Druckformat 14,8 cm x 14,8 cm, Endformat 15,0 x 15,0 cm
- Spiralbindung an der Kopfseite
- doppelseitiges Deckblatt und Rückseite
- 16 Seiten Inhalt, wobei lediglich die Vorderseiten Text enthalten
- Schriftart (optimal Avenir Next, alternativ Arial) und Farbschema laut Corporate Design
- Der Text ist vorgegeben, die Gestaltung ist im Rahmen des Corporate Designs frei
Es soll eine ansprechende Broschüre gestaltet werden, welche die Leser*innen zum Blättern einlädt. Das bedeutet, dass alle Seiten (Deckblatt, Inhaltsseiten und Rückseiten) bei der Gestaltung berücksichtigt werden müssen.
Am Ende soll neben den üblichen Dateien auch eine fertige Druckdatei (siehe Datenblatt) zur Verfügung gestellt werden. Dabei ist zu beachten, dass die Spiralbindung des fertigen Produkts an der Kopfseite sein soll.

```html
<!DOCTYPE html>
<html lang="de">
<head>
<meta charset="utf-8">
<title>Umformulierungen – Leitfaden geschlechtergerechte Sprache</title>
<link rel="stylesheet" href="https://fonts.googleapis.com/css2?family=Nunito+Sans:wght@400;700;800&display=swap">
<style>
  :root {
    --brand-green: #03524a;
    --accent-mint: #a3c2bb;
    --text-grey: #5f5f5f;
    --page-white: #ffffff;
    --frame-grey: #c8c8c8;
  }
  html, body {
    margin: 0;
    padding: 0;
    width: 1200px;
    height: 1200px;
    overflow: hidden;
    background: var(--page-white);
  }
  .page {
    position: relative;
    width: 1200px;
    height: 1200px;
    box-sizing: border-box;
    border: 1px solid var(--frame-grey);
    font-family: "Nunito Sans", "Avenir Next", Arial, sans-serif;
    background: var(--page-white);
  }
  .intro-band {
    position: absolute;
    left: 0; top: 0;
    width: 100%;
    height: 383px;
    background: var(--brand-green);
    color: var(--page-white);
  }
  .intro-title {
    position: absolute;
    left: 81px; top: 122px;
    margin: 0;
    font-size: 36px;
    font-weight: 800;
    letter-spacing: 0.3px;
    line-height: 1;
  }
  .intro-text {
    position: absolute;
    left: 81px; top: 178px;
    width: 900px;
    margin: 0;
    font-size: 26.5px;
    line-height: 42px;
    font-weight: 400;
  }
  .intro-text strong {
    color: var(--accent-mint);
    font-weight: 700;
  }
  .comparison {
    position: absolute;
    top: 446px;
    left: 81px;
    right: 40px;
    display: flex;
  }
  .comparison-column {
    width: 543px;
  }
  .column-heading {
    margin: 0 0 4px;
    color: var(--brand-green);
    font-size: 33px;
    font-weight: 800;
    line-height: 44px;
  }
  .phrase-list {
    list-style: none;
    margin: 0;
    padding: 0;
    color: var(--text-grey);
    font-size: 27px;
    line-height: 40px;
    letter-spacing: 0.2px;
  }
</style>
</head>
<body>
  <main class="page">
    <section class="intro-band">
      <h1 class="intro-title">UMFORMULIERUNGEN</h1>
      <p class="intro-text">Je nach Text oder Zusammenhang bieten sich auch <strong>kreative Umformulierungen</strong> an, um alle Geschlechter gleichermaßen anzusprechen. Zum Beispiel:</p>
    </section>

    <section class="comparison">
      <div class="comparison-column">
        <h2 class="column-heading">statt:</h2>
        <ul class="phrase-list">
          <li>Es gab 20 Teilnehmer</li>
          <li>Ansprechpartner ist …</li>
          <li>Freiwillige Helfer benötigt</li>
          <li>Herausgeber</li>
          <li>Unterstützung durch Kollegen</li>
          <li>Ein Projektleiter sollte darauf<br>achten, …</li>
          <li>Bewerber sollten …</li>
        </ul>
      </div>
      <div class="comparison-column">
        <h2 class="column-heading">besser:</h2>
        <ul class="phrase-list">
          <li>Teilgenommen haben 20 Personen</li>
          <li>Teilgenommen haben 20 Personen</li>
          <li>Freiwillige Hilfe benötigt</li>
          <li>herausgegeben von …</li>
          <li>kollegiale Unterstützung</li>
          <li>Wer ein Projekt leitet, sollte<br>darauf achten, …</li>
          <li>Wer sich bewirbt, sollte …</li>
        </ul>
      </div>
    </section>
  </main>
</body>
</html>
```